High End Notary Service Business Card Design

Want a professional and elegant/luxurious business card that is clean and simple in the design. A notary is a trusted professional that helps people sign very important documents. The card should be in alignment with this service provided.

Most of the time, service will be for the purchase of a home or refinance of a mortgage

There is NO LOGO. This is aesthetic. A look and feel. Conveying professionalism and concierge level of service.

Target Market(s)

Other business professionals, Lawyers, Escrow Officers, Loan Officers

Industry/Entity Type

Legal

Contact Information for Business Card

This will be a one-sided business card

Colors
35a7d7
3176b5
85cae6
d3a5cc
b868aa
ffffff
0356a4

Requirements
Must have
• Lorena T. Mirabel-Hodgkins
Notary Public

642-871-3094
MirabelSigningDesk@Wexmail.com
Nice to have
• Headshot photo below. Convey the aspect of signing documents. No black cards. Preference is shades of blue: light blue, navy, aqua, gold, white, or lavendar, etc.
Should not have
• No scales or legal scales.

```html
<!DOCTYPE html>
<html lang="en">
<head>
<meta charset="utf-8">
<title>Lorena T. Mirabel-Hodgkins — Notary Public</title>
<link href="https://fonts.googleapis.com/css2?family=Cinzel:wght@400&family=Montserrat:wght@300;400&family=Tinos&display=swap" rel="stylesheet">
<style>
  :root {
    --page-bg: #e9ecef;
    --card-blue: #3176b5;
    --text-light: #85cae6;
    --rule-navy: #0b2f57;
    --icon-navy: #123e6b;
  }
  html, body {
    margin: 0;
    width: 1200px;
    height: 1200px;
    overflow: hidden;
    background: var(--page-bg);
  }
  .stage {
    width: 1200px;
    height: 1200px;
    display: flex;
    align-items: center;
    justify-content: center;
  }
  .business-card {
    position: relative;
    width: 1050px;
    height: 600px;
    background: var(--card-blue);
    border-radius: 36px;
    box-shadow: 0 14px 40px rgba(0,0,0,0.25);
  }
  .identity {
    position: absolute;
    left: 150px;
    top: 250px;
    width: 760px;
  }
  .title-row {
    display: flex;
    align-items: baseline;
    white-space: nowrap;
  }
  .holder-name {
    font-family: "Tinos", "Times New Roman", serif;
    font-size: 38px;
    letter-spacing: 0.5px;
    color: var(--text-light);
    text-transform: uppercase;
  }
  .divider-bar {
    display: inline-block;
    width: 3px;
    height: 26px;
    background: var(--icon-navy);
    margin: 0 12px;
    align-self: center;
  }
  .role {
    font-family: "Montserrat", Arial, sans-serif;
    font-weight: 400;
    font-size: 16px;
    letter-spacing: 3px;
    color: var(--text-light);
    text-transform: uppercase;
  }
  .rule {
    height: 2px;
    background: var(--rule-navy);
    margin: 6px 0 10px 18px;
  }
  .contact-row {
    display: flex;
    align-items: center;
    gap: 10px;
    margin-left: 24px;
    font-family: "Montserrat", Arial, sans-serif;
    font-weight: 400;
    font-size: 20px;
    letter-spacing: 2.5px;
    color: var(--text-light);
    white-space: nowrap;
  }
  .contact-row svg { width: 18px; height: 18px; flex: none; }
  .sep { margin: 0 10px; color: var(--icon-navy); }
</style>
</head>
<body>
<main class="stage">
  <section class="business-card">
    <div class="identity">
      <div class="title-row">
        <span class="holder-name">Lorena T. Mirabel-Hodgkins</span>
        <span class="divider-bar"></span>
        <span class="role">Notary Public</span>
      </div>
      <div class="rule"></div>
      <div class="contact-row">
        <svg viewBox="0 0 24 24" aria-hidden="true"><path fill="#123e6b" d="M6.6 10.8a15.1 15.1 0 006.6 6.6l2.2-2.2c.3-.3.7-.4 1-.2 1.1.4 2.3.6 3.6.6.6 0 1 .4 1 1V20c0 .6-.4 1-1 1A17 17 0 013 4c0-.6.4-1 1-1h3.5c.6 0 1 .4 1 1 0 1.3.2 2.5.6 3.6.1.3 0 .7-.2 1z"/></svg>
        <span class="phone">642-871-3094</span>
        <span class="sep">|</span>
        <svg viewBox="0 0 24 24" aria-hidden="true"><rect x="2" y="5" width="20" height="14" rx="1.5" fill="none" stroke="#123e6b" stroke-width="2"/><path d="M2 6l10 7 10-7" fill="none" stroke="#123e6b" stroke-width="2"/></svg>
        <span class="email">MirabelSigningDesk@Wexmail.com</span>
      </div>
    </div>
  </section>
</main>
</body>
</html>
```